1 Page Sales Brochure of our Services

I need to create a one page brochure that our sales team can take into meetings about our services - Need this to be an impressive one page that looks fresh and new using our brand colors of Brindle green, black and white. Our brand looks "clean" think Marlo brand in how everything is clean and white and crisp. Our website showcases our services: https://brindlesports.example/services/ --- After done with this project I would like to create a full booklet. Want to begin with this project first.

Target Market(s)

State of Texas

Industry/Entity Type

Sports Construction in Texas Only

Font styles to use
Serif

Colors
00AB8E
00BBA5
67D7C9
C6EFE9
E9F9F6

Requirements
Must have
• Front and Back and cover our services outlined on our website: https://brindlesports.example/services/
Nice to have
• Need one that can get sent digital and printed -- Our colors are the Brindle green, white and black - We want brochure to look clean, almost like the Marlo feel of their product's branding

```html
<!DOCTYPE html>
<html lang="en">
<head>
<meta charset="utf-8">
<title>Brindle Sports Construction – Services Brochure</title>
<link href="https://fonts.googleapis.com/css2?family=Montserrat:wght@400;600;700;900&family=Oswald:wght@500&display=swap" rel="stylesheet">
<style>
:root{
  --brand-green:#0d6a33;
  --brand-green-dark:#0a5428;
  --ink:#1f1f1f;
  --text:#333333;
  --paper:#ffffff;
  --canvas:#ffffff;
  --placeholder:#d9dcdb;
  --placeholder-dark:#b9bebc;
}
*{margin:0;padding:0;box-sizing:border-box}
html,body{width:1200px;height:3012px;overflow:hidden;background:var(--canvas)}
body{position:relative;font-family:"Montserrat",Arial,sans-serif;color:var(--text)}
.page{position:absolute;left:122px;width:958px;height:1357px;background:var(--paper);box-shadow:0 10px 30px rgba(0,0,0,.35);overflow:hidden}
.page--front{top:114px}
.page--back{top:1562px}
.abs{position:absolute}

/* brand */
.brand{left:0;width:958px;top:50px;text-align:center;color:var(--brand-green);font-family:"Oswald",Arial,sans-serif;font-weight:500}
.brand__mark{display:inline-block;width:44px;height:44px;border-radius:50%;background:var(--brand-green);vertical-align:middle;margin-right:14px}
.brand__name{font-size:78px;line-height:1;vertical-align:middle}
.brand__tag{display:block;font-size:24px;letter-spacing:1px;margin-top:4px;padding-left:120px}

/* hero */
.hero-band{left:0;top:308px;width:958px;height:219px;background:var(--ink)}
.hero-title{left:79px;top:213px;width:801px;height:245px;background:linear-gradient(135deg,#0f7538,#0b5e2c);display:flex;flex-direction:column;align-items:center;justify-content:center;text-align:center;color:#fff;font-weight:900;font-size:70px;line-height:1.1;letter-spacing:-1px}
.hero-title span{display:block;white-space:nowrap}

/* section heading */
.heading{display:flex;align-items:stretch;height:47px;left:53px}
.heading__bar{width:4px;background:var(--brand-green);margin-right:3px}
.heading__pill{background:var(--brand-green);color:#fff;font-family:"Oswald",Arial,sans-serif;font-weight:500;font-size:33px;line-height:47px;padding:0 16px 0 11px;border-radius:0 24px 24px 0;text-transform:uppercase;letter-spacing:-.3px;white-space:nowrap}

.copy{font-size:10.6px;line-height:13.6px;color:var(--text)}
.copy p+p{margin-top:10px}

.photo{border-radius:30px 0 30px 0}

/* partner placeholders */
.partners{left:53px;width:855px;height:70px;display:flex;align-items:center;justify-content:space-between}
.partner-slot{display:block;background:var(--placeholder)}
.partner-slot--circle{width:68px;height:68px;border-radius:50%;background:var(--placeholder-dark)}
.partner-slot--wide{width:132px;height:30px;border-radius:4px}
.partner-slot--bar{width:112px;height:24px;border-radius:4px}
.partner-slot--square{width:62px;height:44px;border-radius:3px;background:var(--placeholder-dark)}
.partner-slot--oval{width:104px;height:50px;border-radius:50%}

/* footer */
.footer{left:0;top:1255px;width:958px;height:102px}
.footer svg{position:absolute;left:0;top:0}
.contacts{position:absolute;left:60px;top:34px;display:flex;align-items:center;color:#fff;font-weight:700;font-size:13px}
.contact{display:flex;align-items:center;margin-right:22px}
.contact svg{position:static;margin-right:14px}
</style>
</head>
<body>

<section class="page page--front">
  <div class="abs brand">
    <span class="brand__mark"></span><span class="brand__name">Brindle</span>
    <span class="brand__tag">Sports Construction</span>
  </div>

  <div class="abs hero-band"></div>
  <h1 class="abs hero-title"><span>BUILDING TO A</span><span>HIGHER STANDARD</span></h1>

  <div class="abs heading" style="top:552px"><span class="heading__bar"></span><span class="heading__pill">Our Services</span></div>
  <div class="abs copy" style="left:53px;top:613px;width:854px">
    <p>Brindle Sports Construction offers turnkey solutions in the realm of general sports construction. We're committed to excellence in all we do, and we seek to develop lasting relationships with our clients. Brindle is not in the business to win a single job and move on. We are working to earn your trust and business as we want you as a customer for life.</p>
    <p>At Brindle we have 7 Proverbs we strive to live by. Our #1 proverb is to "Deliver On Our Promises". That is our promise to you that we will strive to deliver on time with the quality and service you expect and deserve on every job.</p>
  </div>

  <div class="abs heading" style="top:701px"><span class="heading__bar"></span><span class="heading__pill">Track Construction</span></div>
  <div class="abs photo" role="img" aria-label="Aerial view of a stadium with a green turf field and red running track" style="left:605px;top:700px;width:282px;height:191px;background:linear-gradient(160deg,#b8c3cc 0%,#3e8a3c 35%,#2f7a33 60%,#9a3b32 80%,#6c6f73 100%)"></div>
  <div class="abs copy" style="left:53px;top:759px;width:487px">
    <p>When you're looking to have a track installed at your school or facility, there are many factors that come into play. This is a highly specialized job, and you'll want to work with a team that has the expertise necessary to plan and execute a quality installation. At Brindle, we are proud to offer solutions in track construction for a variety of client types.</p>
    <p>Brindle recommends the Trackline line of running track systems developed by CSG, owned by Fieldline Group, as the industry leaders in high quality, performance-enhancing systems that result in unmatched results for the lifecycle of your track.</p>
  </div>
  <div class="abs copy" style="left:53px;top:895px;width:854px">
    <p>Our track specialists install base mats to full pour systems with custom color options. One of the most popular new features to track systems is alternating exchange zone colors to really make your track stand out. Brindle has chosen to partner with CSG for our track products as we believe they provide the highest quality product on the market today with the most durable and high performing track systems. lifecycle of your track.</p>
  </div>

  <div class="abs heading" style="top:955px"><span class="heading__bar"></span><span class="heading__pill">Natural Grass Fields</span></div>
  <div class="abs photo" role="img" aria-label="Natural grass baseball outfield under a blue sky" style="left:605px;top:947px;width:282px;height:191px;background:linear-gradient(180deg,#5d95d6 0%,#a9c9ea 38%,#8a9a7c 46%,#6f9a3c 55%,#5b8a2e 100%)"></div>
  <div class="abs copy" style="left:53px;top:1017px;width:480px">
    <p>Natural Grass is a growing area of our business and we have brought in natural grass experts to join the Brindle team who understand the challenges involved with installing and maintaining grass fields. Two of our experts are certified field builders with one specializing in both synthetic and natural grass installations. Our team operates with specialized equipment allowing massive amounts of dirt to be moved and graded when building natural grass fields. Due to the specialists on our team, we can assist in the design build of your water system to ensure your natural grass will hold the test of time after our installation is complete. If a natural grass field makes the most sense for your specific venue and application, Brindle can help you to bring that project to life.</p>
  </div>

  <div class="abs partners" style="top:1170px" role="img" aria-label="Partner and certification badges">
    <span class="partner-slot partner-slot--circle"></span>
    <span class="partner-slot partner-slot--wide"></span>
    <span class="partner-slot partner-slot--bar"></span>
    <span class="partner-slot partner-slot--bar"></span>
    <span class="partner-slot partner-slot--bar"></span>
    <span class="partner-slot partner-slot--square"></span>
    <span class="partner-slot partner-slot--oval"></span>
  </div>

  <footer class="abs footer">
    <svg width="958" height="102" viewBox="0 0 958 102">
      <polygon points="0,0 670,0 712,55 958,55 958,102 0,102" fill="#1f1f1f"/>
      <polygon points="696,20 958,20 958,41 712,41" fill="#0d6a33"/>
    </svg>
    <div class="contacts">
      <span class="contact"><svg width="22" height="22" viewBox="0 0 24 24"><path d="M6.6 10.8a15 15 0 0 0 6.6 6.6l2.2-2.2c.3-.3.7-.4 1-.2 1.1.4 2.3.6 3.6.6.6 0 1 .4 1 1V20c0 .6-.4 1-1 1A17 17 0 0 1 3 4c0-.6.4-1 1-1h3.5c.6 0 1 .4 1 1 0 1.3.2 2.5.6 3.6.1.3 0 .7-.2 1z" fill="#fff"/></svg>(555) 010-4420</span>
      <span class="contact"><svg width="20" height="24" viewBox="0 0 20 24"><path d="M10 1a7 7 0 0 0-7 7c0 5.3 7 12 7 12s7-6.7 7-12a7 7 0 0 0-7-7zm0 9.5A2.5 2.5 0 1 1 10 5.5a2.5 2.5 0 0 1 0 5z" fill="#fff"/><ellipse cx="10" cy="22" rx="7" ry="1.6" fill="none" stroke="#fff" stroke-width="1.2"/></svg>48 Meadow Lane</span>
      <span class="contact"><svg width="22" height="22" viewBox="0 0 24 24"><circle cx="12" cy="12" r="10" fill="none" stroke="#fff" stroke-width="2"/><path d="M2 12h20M12 2c3 3 3 17 0 20M12 2c-3 3-3 17 0 20" fill="none" stroke="#fff" stroke-width="1.6"/></svg>www.brindlesports.example</span>
    </div>
  </footer>
</section>

<section class="page page--back">
  <div class="abs heading" style="top:49px"><span class="heading__bar"></span><span class="heading__pill">Synthetic Field Construction</span></div>
  <div class="abs photo" role="img" aria-label="Close-up of synthetic turf installation machinery" style="left:605px;top:47px;width:282px;height:156px;background:linear-gradient(135deg,#6f7b6a,#3f5a3a 45%,#9a9a86 70%,#4d5f45)"></div>
  <div class="abs copy" style="left:53px;top:108px;width:478px">
    <p>With the wide selection of synthetic turf systems– no matter the venue or sport– Brindle has a viable solution.</p>
    <p>Verdant Turf's premium turf system series boasts heavy face weights for the best the industry has to offer in aesthetics, durability, and player protection. These systems are driven by the latest research, and technology pushing the industry towards the most grass-like surfaces available.</p>
  </div>

  <div class="abs heading" style="top:231px"><span class="heading__bar"></span><span class="heading__pill">Stadium Construction</span></div>
  <div class="abs photo" role="img" aria-label="Aerial view of a football stadium with grandstands" style="left:605px;top:225px;width:282px;height:156px;background:linear-gradient(150deg,#c9cdd0 0%,#8d949a 35%,#4f8a45 55%,#a6acb0 80%,#6d7378 100%)"></div>
  <div class="abs copy" style="left:53px;top:301px;width:478px">
    <p>In every sense of the word, Brindle is a one-stop shop for all things sports construction. We are a true turn-key construction company owned and operated by seasoned professionals who care. From ground-up stadium construction to total lifecycle planning, we provide custom construction solutions through all stages of your projects.</p>
  </div>

  <div class="abs heading" style="top:405px"><span class="heading__bar"></span><span class="heading__pill">Tennis Court Construction</span></div>
  <div class="abs photo" role="img" aria-label="Blue tennis courts lined with pine trees" style="left:605px;top:403px;width:282px;height:156px;background:linear-gradient(180deg,#3b76c9 0%,#5e93d8 25%,#2c4a2a 40%,#2f5b8e 70%,#2f6cc0 90%,#4b8a3a 100%)"></div>
  <div class="abs copy" style="left:53px;top:471px;width:478px">
    <p>To ensure that our customers are playing on the best tennis courts available, we've partnered with CSG to provide Courtex court surfacing systems. Courtex offers a variety of impact reducing, performance enhancing court systems that are of the highest quality in the industry. Learn more about why Courtex is the top choice for tennis court construction, and contact us to get started on your tennis court project today.</p>
  </div>

  <div class="abs heading" style="top:586px"><span class="heading__bar"></span><span class="heading__pill">Service + Maintenance</span></div>
  <div class="abs photo" role="img" aria-label="Worker inspecting a synthetic turf field" style="left:605px;top:586px;width:282px;height:156px;background:linear-gradient(180deg,#d4d8dc 0%,#a7b0b5 30%,#3f7a33 45%,#2f6a28 100%)"></div>
  <div class="abs copy" style="left:53px;top:650px;width:478px">
    <p>Brindle Sports is here to support you throughout the entire lifecycle of your sports construction projects from conception to intermittent servicing when needed. We provide maintenance services and support for all sports surfaces, helping you protect your investment and extend the life of your synthetic turf, track or tennis court through education, performance testing, and maintenance services. It's important to us that each customer gets the most out of their sports surfaces, that peak performance, safety, and ease of maintenance are a part of the customer experience. That is our ongoing commitment to you.</p>
  </div>

  <div class="abs heading" style="top:788px"><span class="heading__bar"></span><span class="heading__pill">Stadium Lighting</span></div>
  <div class="abs photo" role="img" aria-label="Before and after comparison of a field under old and LED stadium lighting" style="left:605px;top:782px;width:282px;height:156px;background:linear-gradient(90deg,#5d6e3a 0%,#7a8a4a 49%,#2a2f2a 50%,#6fa85a 75%,#3d5a33 100%)"></div>
  <div class="abs copy" style="left:53px;top:852px;width:478px">
    <p>Brindle also provides lighting services. Take advantage of the energy efficiency and cost savings by converting to LED lighting. According to national energy studies, light-emitting diodes (LED) are six to seven times more energy efficient than conventional light bulbs and cut energy use by more than 80 percent. LED light bulbs can also last 25,000 hours or more, which is 25 times longer than traditional bulbs. You can see why LED lighting makes financial sense!</p>
  </div>

  <div class="abs heading" style="top:987px"><span class="heading__bar"></span><span class="heading__pill">Surface Maintenance + Repair</span></div>
  <div class="abs photo" role="img" aria-label="Grooming machine working on a purple and green synthetic field" style="left:605px;top:987px;width:282px;height:156px;background:linear-gradient(170deg,#bfc6cc 0%,#8a9a70 20%,#3f8a3a 35%,#6a3a9a 60%,#5a2e8a 100%)"></div>
  <div class="abs copy" style="left:53px;top:1051px;width:478px">
    <p>All sports systems involve some component of maintenance to ensure your surface is performing properly and will withstand the test of time. Many of our synthetic fields undergo annual field maintenance and bacterial and COVID killing sprays. This is particularly important for athletes who will be using indoor facilities as they do not receive sunlight which aids in killing bacteria. If you would like to have a free maintenance or field/surface evaluation, please email us at aftercare@brindlesports.example.</p>
  </div>

  <div class="abs partners" style="top:1169px" role="img" aria-label="Partner and certification badges">
    <span class="partner-slot partner-slot--circle"></span>
    <span class="partner-slot partner-slot--wide"></span>
    <span class="partner-slot partner-slot--bar"></span>
    <span class="partner-slot partner-slot--bar"></span>
    <span class="partner-slot partner-slot--bar"></span>
    <span class="partner-slot partner-slot--square"></span>
    <span class="partner-slot partner-slot--oval"></span>
  </div>

  <footer class="abs footer">
    <svg width="958" height="102" viewBox="0 0 958 102">
      <polygon points="0,0 670,0 712,55 958,55 958,102 0,102" fill="#1f1f1f"/>
      <polygon points="696,20 958,20 958,41 712,41" fill="#0d6a33"/>
    </svg>
    <div class="contacts">
      <span class="contact"><svg width="22" height="22" viewBox="0 0 24 24"><path d="M6.6 10.8a15 15 0 0 0 6.6 6.6l2.2-2.2c.3-.3.7-.4 1-.2 1.1.4 2.3.6 3.6.6.6 0 1 .4 1 1V20c0 .6-.4 1-1 1A17 17 0 0 1 3 4c0-.6.4-1 1-1h3.5c.6 0 1 .4 1 1 0 1.3.2 2.5.6 3.6.1.3 0 .7-.2 1z" fill="#fff"/></svg>(555) 010-4420</span>
      <span class="contact"><svg width="20" height="24" viewBox="0 0 20 24"><path d="M10 1a7 7 0 0 0-7 7c0 5.3 7 12 7 12s7-6.7 7-12a7 7 0 0 0-7-7zm0 9.5A2.5 2.5 0 1 1 10 5.5a2.5 2.5 0 0 1 0 5z" fill="#fff"/><ellipse cx="10" cy="22" rx="7" ry="1.6" fill="none" stroke="#fff" stroke-width="1.2"/></svg>48 Meadow Lane</span>
      <span class="contact"><svg width="22" height="22" viewBox="0 0 24 24"><circle cx="12" cy="12" r="10" fill="none" stroke="#fff" stroke-width="2"/><path d="M2 12h20M12 2c3 3 3 17 0 20M12 2c-3 3-3 17 0 20" fill="none" stroke="#fff" stroke-width="1.6"/></svg>www.brindlesports.example</span>
    </div>
  </footer>
</section>

</body>
</html>
```